VELQA Business Card Design

I have a rough idea of the design / layout of the company business card but need help in finalizing the design and quality.

I'm looking for the card to be stand out, but simple, on the front with clear detail on the back with space for some one to write any other detail they need onto the card. The rough draft includes the crinkled graph paper back ground which I quite like for the front.

I will need the card design completed and ready to print in Australian business card standard sizes. This includes detail on all colors, fonts and type faces used as well as copy of the original for editing (inserting other employee details).

I have included the company logo and a rough draft of the card, including the graphic I would like to use for the back ground on the front, I am not sure that the graphic is any good for printing, not the highest res.

Thanks,

Lyle

```html
<!DOCTYPE html>
<html lang="en">
<head>
<meta charset="utf-8">
<title>VELQA Business Card</title>
<link rel="stylesheet" href="https://fonts.googleapis.com/css2?family=Exo+2:wght@400;500;600;800&display=swap">
<style>
  :root {
    --stage: #6e6e6e;
    --paper: #ffffff;
    --paper-shade: #e4e4e4;
    --ink: #111111;
    --ink-soft: #3a3a3a;
    --grey-band: #8c8c8c;
  }
  * { margin: 0; padding: 0; box-sizing: border-box; }
  html, body { width: 1200px; height: 750px; overflow: hidden; }
  body {
    background: var(--stage);
    font-family: "Exo 2", sans-serif;
    color: var(--ink);
    display: flex;
    align-items: center;
    justify-content: center;
    gap: 60px;
  }
  .card {
    position: relative;
    width: 520px;
    height: 318px;
    background: radial-gradient(ellipse at 45% 40%, var(--paper) 0%, var(--paper) 45%, var(--paper-shade) 100%);
    overflow: hidden;
  }

  /* Front */
  .card--front {
    display: flex;
    flex-direction: column;
    align-items: center;
    justify-content: center;
  }
  .front__name {
    font-weight: 800;
    font-size: 88px;
    line-height: 1;
    letter-spacing: -2px;
    color: var(--ink);
  }
  .front__web {
    margin-top: 38px;
    font-weight: 500;
    font-size: 15px;
    letter-spacing: 3px;
    color: var(--ink-soft);
  }

  /* Back */
  .back__swoosh { position: absolute; inset: 0; width: 100%; height: 100%; }
  .back__brand {
    position: absolute;
    left: 40px;
    top: 62px;
    font-weight: 800;
    font-size: 58px;
    line-height: 1;
    letter-spacing: -1px;
  }
  .back__rule {
    position: absolute;
    left: 40px;
    top: 142px;
    width: 300px;
    height: 1.5px;
    background: var(--ink);
  }
  .back__person { position: absolute; left: 40px; top: 156px; }
  .person__name {
    font-weight: 600;
    font-size: 15px;
    letter-spacing: 1.5px;
    text-transform: uppercase;
  }
  .person__role {
    font-size: 10px;
    letter-spacing: 1.5px;
    text-transform: uppercase;
    color: var(--ink-soft);
  }
  .person__phones { margin-top: 14px; list-style: none; }
  .contact-line {
    display: flex;
    align-items: center;
    gap: 8px;
    font-size: 13px;
    letter-spacing: 1.5px;
    margin-bottom: 4px;
    white-space: nowrap;
  }
  .contact-line svg { width: 14px; height: 14px; flex: none; }

  .back__details {
    position: absolute;
    right: 40px;
    top: 40px;
    text-align: right;
    width: 190px;
  }
  .details__address { font-size: 11px; letter-spacing: 1px; line-height: 1.4; }
  .details__rule { height: 1.5px; background: var(--ink); margin: 6px 0 8px; }
  .details__online { list-style: none; }
  .details__online .contact-line {
    justify-content: flex-end;
    font-size: 11px;
    letter-spacing: 1px;
    margin-bottom: 6px;
  }
  .details__online .contact-line svg { order: 2; }
</style>
</head>
<body>

  <section class="card card--front" aria-label="Card front">
    <div class="front__name">VELQA</div>
    <div class="front__web">www.velqaav.com</div>
  </section>

  <section class="card card--back" aria-label="Card back">
    <svg class="back__swoosh" viewBox="0 0 520 318" preserveAspectRatio="none" aria-hidden="true">
      <path d="M520 120 C470 230 330 300 150 318 L520 318 Z" fill="#8c8c8c"/>
      <path d="M520 150 C470 250 340 305 200 318 L520 318 Z" fill="#ffffff"/>
      <path d="M520 162 C475 258 350 308 230 318 L520 318 Z" fill="#111111"/>
      <path d="M470 210 C420 260 340 290 270 300 C350 285 420 255 470 215 Z" fill="#ffffff"/>
    </svg>

    <div class="back__brand">VELQA</div>
    <div class="back__rule"></div>

    <div class="back__person">
      <div class="person__name">Corin Halvey</div>
      <div class="person__role">Financial Advisor</div>
      <ul class="person__phones">
        <li class="contact-line">
          <svg viewBox="0 0 16 16" aria-hidden="true"><circle cx="8" cy="8" r="8" fill="#111"/><path d="M5 4.5 l1.5 0 0.6 2 -1 0.8 a5 5 0 0 0 2.6 2.6 l0.8 -1 2 0.6 0 1.5 a1 1 0 0 1 -1 1 A6.5 6.5 0 0 1 4 5.5 a1 1 0 0 1 1 -1 Z" fill="#fff"/></svg>
          013 456 7890
        </li>
        <li class="contact-line">
          <svg viewBox="0 0 16 16" aria-hidden="true"><circle cx="8" cy="8" r="8" fill="#111"/><rect x="5.5" y="3.5" width="5" height="9" rx="1" fill="#fff"/><rect x="6.5" y="5" width="3" height="5" fill="#111"/></svg>
          013 456 7891
        </li>
      </ul>
    </div>

    <div class="back__details">
      <div class="details__address">41 Harbour St, Level 2<br>Sydney NSW</div>
      <div class="details__rule"></div>
      <ul class="details__online">
        <li class="contact-line">
          <svg viewBox="0 0 16 16" aria-hidden="true"><circle cx="8" cy="8" r="8" fill="#111"/><rect x="4" y="5" width="8" height="6" fill="#fff"/><path d="M4 5 L8 8.5 L12 5" stroke="#111" fill="none"/></svg>
          hello@velqaav.com
        </li>
        <li class="contact-line">
          <svg viewBox="0 0 16 16" aria-hidden="true"><circle cx="8" cy="8" r="8" fill="#111"/><circle cx="8" cy="8" r="4.5" fill="none" stroke="#fff"/><ellipse cx="8" cy="8" rx="2" ry="4.5" fill="none" stroke="#fff"/><line x1="3.5" y1="8" x2="12.5" y2="8" stroke="#fff"/></svg>
          www.velqaav.com
        </li>
      </ul>
    </div>
  </section>

</body>
</html>
```